Postcard Design

I am a podiatry clinic specialising in custom 3D laser orthotics and 3D printed orthotics. wanting to get people in for the new year now their private health has reset.

post card to advertise - front - new year, new 3d laser and 3D printed custom orthotics (based off a blue and white theme)

back left - Now that the new year is upon us, Tern Podiatry is coming to you with a special offer of 3D laser custom orthotics FREE through your private health fund*, or upgrade to the latest innovation and technology available by ordering 3D printed custom orthotics.

When you come in to get your new orthotics you will also receive a $50 Stride Hollow voucher to put towards new shoes, so that you can get the best out of your 3D custom orthotics.

*subject to level of cover, annual limits, health fund rules, and processing through VELORN

logo and contact details under

Back right - address space

Bellow is an example of the type of postcard i am looking for except cleaner and orthotics on the front, as well as other projects been done for the business to get a feel of what i am looking for.

Target Market(s)

people with private healthcare.
age 25+

Industry/Entity Type

Clinic

Requirements
Must have
• clean blue theme

```html
<!DOCTYPE html>
<html lang="en">
<head>
<meta charset="utf-8">
<title>Tern Podiatry – New Year Postcard, Back</title>
<link rel="stylesheet" href="https://fonts.googleapis.com/css2?family=Mulish:wght@400;600;700;800;900&family=Questrial&display=swap">
<style>
  :root {
    --navy: #0b2a55;
    --deep-blue: #0a3f8c;
    --mid-blue: #1a7fd6;
    --bright-blue: #39b3ec;
    --white: #ffffff;
    --panel-glass: rgba(255, 255, 255, 0.5);
    --address-bg: #ffffff;
  }
  * { margin: 0; padding: 0; box-sizing: border-box; }
  html, body {
    width: 1200px;
    height: 930px;
    overflow: hidden;
    background: var(--address-bg);
  }
  .postcard-back {
    position: relative;
    width: 1200px;
    height: 930px;
    background: var(--address-bg);
    font-family: "Mulish", sans-serif;
  }
  .offer-panel {
    position: absolute;
    left: 0;
    top: 0;
    width: 588px;
    height: 930px;
    overflow: hidden;
    background:
      radial-gradient(ellipse 70% 45% at 70% 48%, rgba(92, 205, 246, 0.75), transparent 70%),
      radial-gradient(ellipse 60% 40% at 30% 85%, rgba(70, 180, 235, 0.55), transparent 70%),
      linear-gradient(140deg, #0a2f78 0%, #0d5cc0 28%, #1f8ee0 55%, #2a9de4 75%, #1470cf 100%);
  }
  .offer-panel .swirl-backdrop {
    position: absolute;
    inset: 0;
  }
  .edge-strip {
    position: absolute;
    right: 0;
    top: 0;
    width: 27px;
    height: 930px;
    background: linear-gradient(180deg, #0d4fae 0%, #1c86dc 45%, #2a9de4 70%, #1065c8 100%);
  }
  .headline {
    position: absolute;
    left: 0;
    top: 30px;
    width: 556px;
    text-align: center;
    color: var(--white);
    line-height: 1;
  }
  .headline .now {
    display: block;
    font-family: "Questrial", sans-serif;
    font-size: 68px;
    letter-spacing: 10px;
    padding-left: 10px;
  }
  .headline .soft {
    display: block;
    font-family: "Questrial", sans-serif;
    font-size: 30px;
    letter-spacing: 3px;
    margin-top: 4px;
  }
  .headline .strong {
    display: block;
    font-weight: 800;
    font-size: 33px;
    letter-spacing: 1px;
    margin-top: 2px;
  }
  .intro {
    position: absolute;
    left: 21px;
    top: 218px;
    width: 546px;
    text-align: center;
    color: var(--white);
    font-weight: 700;
    font-size: 18px;
    letter-spacing: 0.6px;
  }
  .free-offer {
    position: absolute;
    left: 0;
    top: 252px;
    width: 556px;
    text-align: center;
    color: var(--navy);
    line-height: 1;
  }
  .free-offer .free {
    display: block;
    font-weight: 900;
    font-size: 66px;
    letter-spacing: 2px;
    color: var(--navy);
    -webkit-text-stroke: 2px var(--white);
    paint-order: stroke fill;
  }
  .free-offer .product {
    display: block;
    font-weight: 800;
    font-size: 28px;
    letter-spacing: 3px;
    line-height: 30px;
    margin-top: 4px;
  }
  .free-offer .fund {
    display: block;
    font-weight: 800;
    font-size: 18px;
    letter-spacing: 0.4px;
    margin-top: 6px;
  }
  .upgrade {
    position: absolute;
    left: 39px;
    top: 497px;
    width: 495px;
    color: var(--white);
    font-weight: 700;
    font-size: 17.5px;
    line-height: 23px;
    letter-spacing: 0.6px;
    text-align: justify;
    text-align-last: justify;
  }
  .voucher-box {
    position: absolute;
    left: 21px;
    top: 585px;
    width: 531px;
    height: 159px;
    background: var(--panel-glass);
    padding: 18px 14px 0 14px;
    color: var(--navy);
    font-weight: 600;
    font-size: 17.5px;
    line-height: 37px;
    text-align: justify;
    text-align-last: center;
    letter-spacing: 0.3px;
  }
  .voucher-box .amount {
    font-family: "Questrial", sans-serif;
    font-size: 34px;
    vertical-align: -3px;
  }
  .footnote {
    position: absolute;
    left: 21px;
    top: 774px;
    width: 380px;
    color: var(--white);
    font-weight: 700;
    font-size: 13px;
    line-height: 20px;
  }
  .brand-name {
    position: absolute;
    right: 24px;
    bottom: 40px;
    color: var(--white);
    font-weight: 800;
    font-size: 34px;
    letter-spacing: 1px;
  }
</style>
</head>
<body>
  <main class="postcard-back">
    <section class="offer-panel">
      <div class="swirl-backdrop" role="img" aria-label="Soft blue swirling abstract background"></div>

      <h1 class="headline">
        <span class="now">Now</span>
        <span class="soft">that the</span>
        <span class="soft">new year</span>
        <span class="strong">is upon us,</span>
      </h1>

      <p class="intro">Tern Podiatry is coming to you with a special offer of</p>

      <p class="free-offer">
        <span class="free">FREE</span>
        <span class="product">3D laser<br>custom<br>orthotics</span>
        <span class="fund">through your private health fund*</span>
      </p>

      <p class="upgrade">or upgrade to the latest innovation and technology available by ordering 3D printed custom orthotics</p>

      <p class="voucher-box">When you come in to get your new orthotics you will also receive a <span class="amount">$50</span> Stride Hollow voucher to put towards new shoes, so that you can get the best out of your 3D custom orthotics.</p>

      <p class="footnote">*subject to level of cover, annual limits, health fund rules, and processing through VELORN</p>

      <p class="brand-name">Tern Podiatry</p>
    </section>

    <div class="edge-strip"></div>
  </main>
</body>
</html>
```